Business Card Design

We are a state licensed general contractor on the south east coast of Florida. We are a remodeling and home repairs business that have been in business for 14 years. Since we are located on the coast and our business name is Ridgeline Builders of Pine Hollow, Inc, we would like a "Ridgeline" themed design that would appeal to more affluent customers. I would like to see light blue colors with waves incorporated into the design. I would also like the design to communicate a modern, confident, responsible company character.

Industry/Entity Type

Contractor

Contact Information for Business Card

Tim Wexler 555-274-9183

```html
<!DOCTYPE html>
<html lang="en">
<head>
<meta charset="utf-8">
<title>Ridgeline Builders – Business Card</title>
<link rel="stylesheet" href="https://fonts.googleapis.com/css2?family=Exo+2:wght@400;500;600;700&display=swap">
<style>
  :root {
    --sky: #1b8fd8;
    --navy: #0b3676;
    --white: #ffffff;
    --ink-grey: #5a5f66;
    --canvas: #e4e6ea;
  }
  * { margin: 0; padding: 0; box-sizing: border-box; }
  html, body {
    width: 1200px; height: 1056px; overflow: hidden;
    background: var(--canvas);
    font-family: "Exo 2", Arial, sans-serif;
  }
  .sheet {
    position: relative; width: 1200px; height: 1056px;
    display: flex; flex-direction: column; align-items: center;
    justify-content: center; gap: 32px;
  }
  .card {
    position: relative; width: 840px; height: 480px;
    background: var(--white); overflow: hidden;
    box-shadow: 0 6px 18px rgba(0,0,0,0.18);
  }
  .card__shapes { position: absolute; inset: 0; width: 100%; height: 100%; }

  /* front */
  .contact {
    position: absolute; color: var(--white);
    font-size: 15px; font-weight: 500; letter-spacing: 0.4px;
    white-space: nowrap; line-height: 1.35;
  }
  .contact svg { display: block; width: 20px; height: 20px; margin-bottom: 8px; fill: var(--white); }
  .contact--phone { left: 34px; top: 38px; }
  .contact--mobile { left: 286px; top: 96px; }
  .contact--web { left: 24px; top: 226px; }
  .contact--address { left: 262px; top: 214px; }
  .contact--email { left: 40px; top: 404px; }

  .identity { position: absolute; left: 520px; top: 86px; }
  .identity__name { color: var(--sky); font-size: 30px; font-weight: 700; letter-spacing: 1.5px; }
  .identity__title { color: var(--ink-grey); font-size: 21px; font-weight: 500; letter-spacing: 1px; margin-top: 2px; }

  .brand { position: absolute; display: flex; align-items: center; gap: 12px; white-space: nowrap; }
  .brand__dot { width: 30px; height: 30px; border-radius: 50%; background: var(--sky); flex: none; }
  .brand__name { color: var(--navy); font-size: 32px; font-weight: 700; letter-spacing: 0.5px; }
  .card--front .brand { left: 462px; top: 236px; }
  .card--back .brand { left: 170px; top: 150px; }

  .website {
    position: absolute; right: 40px; top: 232px;
    color: var(--white); font-size: 22px; font-weight: 500; letter-spacing: 0.8px;
    white-space: nowrap;
    transform: rotate(-10deg); transform-origin: right center;
  }
</style>
</head>
<body>
<main class="sheet">

  <section class="card card--front" aria-label="Business card front">
    <svg class="card__shapes" viewBox="0 0 840 480" aria-hidden="true">
      <polygon fill="var(--sky)" points="420,0 840,0 840,6 420,48"/>
      <polygon fill="var(--sky)" points="0,0 420,0 420,480 0,480"/>
      <polygon fill="var(--navy)" points="420,10 420,170 120,170"/>
      <polygon fill="var(--navy)" points="0,170 120,170 0,214"/>
      <polygon fill="var(--navy)" points="250,170 420,170 420,330 236,330"/>
      <polygon fill="var(--navy)" points="0,330 420,330 420,356 0,392"/>
    </svg>

    <div class="contact contact--phone">
      <svg viewBox="0 0 24 24"><path d="M6.6 10.8a15.1 15.1 0 0 0 6.6 6.6l2.2-2.2c.3-.3.7-.4 1-.2 1.1.4 2.3.6 3.6.6.6 0 1 .4 1 1V20c0 .6-.4 1-1 1A17 17 0 0 1 3 4c0-.6.4-1 1-1h3.5c.6 0 1 .4 1 1 0 1.3.2 2.5.6 3.6.1.3 0 .7-.2 1z"/></svg>
      555-274-9183
    </div>
    <div class="contact contact--mobile">
      <svg viewBox="0 0 24 24"><path d="M7 2h10a2 2 0 0 1 2 2v16a2 2 0 0 1-2 2H7a2 2 0 0 1-2-2V4a2 2 0 0 1 2-2zm0 3v13h10V5zm5 14.2a1 1 0 1 0 0 .1z"/></svg>
      555-274-9183
    </div>
    <div class="contact contact--web">
      <svg viewBox="0 0 24 24"><path d="M12 2a10 10 0 1 0 0 20 10 10 0 0 0 0-20zm6.9 6h-3a15 15 0 0 0-1.3-3.9A8 8 0 0 1 18.9 8zM12 4c.8 1.2 1.5 2.5 1.9 4h-3.8c.4-1.5 1.1-2.8 1.9-4zM4.3 14a8 8 0 0 1 0-4h3.4a16 16 0 0 0 0 4zm.8 2h3a15 15 0 0 0 1.3 3.9A8 8 0 0 1 5.1 16zm3-8h-3a8 8 0 0 1 4.3-3.9C8.9 5.3 8.4 6.6 8.1 8zM12 20c-.8-1.2-1.5-2.5-1.9-4h3.8c-.4 1.5-1.1 2.8-1.9 4zm2.3-6H9.7a14 14 0 0 1 0-4h4.6a14 14 0 0 1 0 4zm.3 5.9c.6-1.2 1-2.5 1.3-3.9h3a8 8 0 0 1-4.3 3.9zm1.7-5.9a16 16 0 0 0 0-4h3.4a8 8 0 0 1 0 4z"/></svg>
      www.ridgelinebuilders.com
    </div>
    <div class="contact contact--address">
      <svg viewBox="0 0 24 24"><path d="M12 2a7 7 0 0 0-7 7c0 5.2 7 13 7 13s7-7.8 7-13a7 7 0 0 0-7-7zm0 9.5a2.5 2.5 0 1 1 0-5 2.5 2.5 0 0 1 0 5z"/></svg>
      14 Harbor Rd,<br>Suite 3, Pine Hollow
    </div>
    <div class="contact contact--email">
      <svg viewBox="0 0 24 24"><path d="M3 5h18a1 1 0 0 1 1 1v12a1 1 0 0 1-1 1H3a1 1 0 0 1-1-1V6a1 1 0 0 1 1-1zm9 7.5L4.5 7.3V17h15V7.3z"/></svg>
      tim@ridgelinebuilders.com
    </div>

    <div class="identity">
      <p class="identity__name">TIM WEXLER</p>
      <p class="identity__title">GENERAL MANAGER</p>
    </div>

    <div class="brand">
      <span class="brand__dot"></span>
      <span class="brand__name">Ridgeline Builders</span>
    </div>
  </section>

  <section class="card card--back" aria-label="Business card back">
    <svg class="card__shapes" viewBox="0 0 840 480" aria-hidden="true">
      <polygon fill="var(--sky)" points="560,0 840,0 840,40"/>
      <polygon fill="var(--navy)" points="0,372 840,138 840,300 520,330 0,410"/>
      <polygon fill="var(--sky)" points="0,420 600,346 0,480"/>
    </svg>

    <div class="brand">
      <span class="brand__dot"></span>
      <span class="brand__name">Ridgeline Builders</span>
    </div>

    <p class="website">www.ridgelinebuilders.com</p>
  </section>

</main>
</body>
</html>
```